Website for B2B SaaS Financial Segmentation Service

I need a website that explains a service I provide called Lumen Ladder Review and gives visitors a professional-looking opt-in form for my Keap CRM. I also want it to have a CMS that I can easily edit when I want to update images and copy.

Lumen Ladder Review is a dashboard I produce that gives B2B SaaS executives an economic segmentation of their active revenue build. It breaks the revenue build into 3 categories and illustrates how much of the revenue build is in each category.

The red category is customers who have not repaid what I call "Poor Man's" cost of revenue and are therefore unprofitable.

The green category is customers who have repaid Poor Man's cost of revenue and are therefore profitable.

The blue category is customers who have repaid Poor Man's cost of revenue, but are deceptively unprofitable for the business because of how much servicing them costs.

I call the green category the "Center of Solvency."

The website will contain descriptions of the overall concept and each of the categories and have lots of calls to action that get them to engage with me through the opt-in form.

I might also be interested in a live chat feature for the site, but not if that is an expensive monthly option.

Target Market(s)

B2B SaaS companies

Industry/Entity Type

B2B SaaS

Coding

Coded - Design and coding required

Number of Pages Required

3 page

Requirements
Must have
• A strong landing page with a good drill-down page I can reuse and a blog I can post to. Color schema that matches the logo I uploaded.

```html
<!DOCTYPE html>
<html lang="en">
<head>
<meta charset="utf-8">
<title>Lumen Ladder Review</title>
<link href="https://fonts.googleapis.com/css2?family=Catamaran:wght@500;600;700;800&family=Roboto:wght@400;500;700&display=swap" rel="stylesheet">
<style>
:root{
  --teal:#10c3a4;
  --teal-dark:#0aa592;
  --blue:#2f7cf6;
  --blue-band:#2a6ff5;
  --red:#e2191c;
  --ink:#111;
  --muted:#666;
  --white:#fff;
  --hero:#0b1722;
}
*{box-sizing:border-box;margin:0;padding:0}
html,body{width:1200px;height:2962px;overflow:hidden;background:var(--white)}
body{position:relative;font-family:"Roboto",sans-serif;color:var(--ink)}
.abs{position:absolute}
.top-rule{left:0;top:0;width:1200px;height:4px;background:var(--red)}
.btn{position:absolute;display:flex;align-items:center;justify-content:center;height:42px;width:126px;border-radius:21px;color:var(--white);font:700 16px "Roboto",sans-serif}
.btn-blue{background:linear-gradient(90deg,#4a8dfb,var(--blue))}
.btn-teal{background:linear-gradient(90deg,var(--teal-dark),var(--teal))}
.brand{display:flex;align-items:center;gap:10px;font:700 17px "Catamaran",sans-serif;letter-spacing:3px;text-transform:uppercase;color:#1c2530}
.brand-mark{width:14px;height:14px;background:var(--teal)}
.nav{display:flex;font-size:16px;color:#444}
.nav span{position:absolute;white-space:nowrap}
/* hero */
.hero{left:0;top:163px;width:1200px;height:602px;background:radial-gradient(ellipse at 60% 40%,#1c3a4a 0%,#0d1f2b 45%,#05090d 100%)}
.hero-text{left:0;width:1200px;text-align:center;color:var(--white)}
.hero-kicker{top:255px;font:600 48px "Catamaran",sans-serif}
.hero-title{top:318px;font:800 64px "Catamaran",sans-serif}
.hero-copy{left:165px;top:420px;width:870px;text-align:center;color:var(--white);font-size:15px;line-height:28px}
.mouse{left:586px;top:655px;width:28px;height:56px;border-radius:14px;background:var(--white)}
/* about */
.about-block{left:56px;top:1026px;width:394px;height:342px;background:var(--teal)}
.about-photo{left:110px;top:866px;width:436px;height:445px;background:linear-gradient(160deg,#2b2f5c 0%,#1d3a66 45%,#a0302e 80%,#1a1520 100%)}
h2{font:800 50px "Catamaran",sans-serif;text-transform:uppercase;color:var(--ink)}
.about-title{left:600px;top:850px}
.body-text{font-size:14px;line-height:26.5px;color:var(--muted)}
.about-p1{left:600px;top:927px;width:490px}
.about-p2{left:600px;top:1113px;width:490px}
/* categories */
.cat-title{left:0;top:1515px;width:1200px;text-align:center}
.cat-intro{left:170px;top:1588px;width:860px;text-align:center;font-size:15px;line-height:28px;color:var(--muted)}
.cat-name{font:700 28px/36px "Catamaran",sans-serif;text-align:right}
.badge{width:62px;height:62px;border-radius:50%;display:flex;align-items:center;justify-content:center}
.badge i{width:44px;height:44px;border-radius:50%;display:flex;align-items:center;justify-content:center;color:var(--white);font:700 16px "Roboto",sans-serif;font-style:normal}
.cat-desc{font-size:14px;line-height:26px;color:var(--muted);text-align:right}
/* contact */
.contact{left:0;top:2383px;width:1200px;height:252px;background:linear-gradient(100deg,#2d66f0,var(--blue-band) 50%,#3b7bf8)}
.contact-title{left:110px;top:2450px;color:var(--white);font:700 52px/64px "Catamaran",sans-serif}
.field{position:absolute;width:287px;height:46px;border:1px solid rgba(255,255,255,.85);color:var(--white);font-size:14px;display:flex;align-items:center;padding-left:15px}
.submit{position:absolute;width:287px;height:46px;background:var(--white);color:var(--blue);font:500 16px "Roboto",sans-serif;display:flex;align-items:center;justify-content:center}
/* footer */
.footer{left:0;top:2635px;width:1200px;height:327px;background:#000}
.foot-nav span{position:absolute;top:2820px;color:var(--white);font-size:16px;white-space:nowrap}
.social{width:30px;height:30px;border-radius:50%;background:var(--white)}
.copy{left:0;top:2918px;width:1200px;text-align:center;color:var(--white);font-size:12px}
.chat{left:1124px;top:2842px;width:50px;height:50px;border-radius:50%;background:var(--red);display:flex;align-items:center;justify-content:center}
</style>
</head>
<body>
<div class="abs top-rule"></div>

<header>
  <div class="abs brand" style="left:110px;top:66px"><span class="brand-mark"></span>Lumen Ladder Review</div>
  <a class="btn btn-blue" style="left:816px;top:38px">Contact Us</a>
  <a class="btn btn-teal" style="left:962px;top:38px">Get Started</a>
  <nav class="nav">
    <span style="left:464px;top:101px">Home</span>
    <span style="left:567px;top:101px">About Us</span>
    <span style="left:691px;top:101px">Our Categories</span>
    <span style="left:855px;top:101px">Testimonials</span>
    <span style="left:1003px;top:101px">Latest Blogs</span>
  </nav>
</header>

<section>
  <div class="abs hero" role="img" aria-label="Dark finance backdrop with rising arrows, candlestick chart and a hand touching a screen"></div>
  <div class="abs hero-text hero-kicker">WELCOME TO</div>
  <div class="abs hero-text hero-title">LUMEN LADDER REVIEW</div>
  <p class="abs hero-copy">Nemo enim ipsam voluptatem quia voluptas sit aspernatur aut odit aut fugit, sed quia consequuntur magni dolores eos qui ratione voluptatem sequi nesciunt. Neque porro quisquam est, qui dolorem ipsum quia dolor sit amet, consectetur, adipisci velit, sed quia non numquam eius modi tempora incidunt ut labore et dolore magnam aliquam</p>
  <a class="btn btn-teal" style="left:537px;top:528px">Get Started</a>
  <div class="abs mouse">
    <svg width="28" height="56" viewBox="0 0 28 56"><rect x="8" y="14" width="12" height="18" rx="6" fill="none" stroke="#222" stroke-width="1.5"/><line x1="14" y1="18" x2="14" y2="23" stroke="#222" stroke-width="1.5"/><path d="M14 36v9M11 42l3 3 3-3" fill="none" stroke="#222" stroke-width="1.5"/></svg>
  </div>
</section>

<section>
  <div class="abs about-block"></div>
  <div class="abs about-photo" role="img" aria-label="Open hand holding a rising bar chart with an upward arrow against city lights"></div>
  <h2 class="abs about-title">About Us</h2>
  <p class="abs body-text about-p1">I must explain to you how all this mistaken idea of denouncing pleasure and praising pain was born and I will give you a complete account of the system, and expound the actual teachings of the great explorer of the truth, the master-builder of human happiness. No one rejects, dislikes, or avoids pleasure itself, because it is pleasure, but because those who do not know how to pursue pleasure rationally encounter consequences that are extremely painful.</p>
  <p class="abs body-text about-p2">Nor again is there anyone who loves or pursues or desires to obtain pain of itself, because it is pain, but because occasionally circumstances occur in which toil and pain can procure him some great pleasure. To take a trivial example, which of us ever undertakes laborious physical exercise, except to obtain some advantage from it? But who has any right to find fault with a man who chooses to enjoy a pleasure that has no annoying consequences, or one who avoids a pain that produces no resultant pleasure?</p>
  <a class="btn btn-teal" style="left:600px;top:1330px">Read More</a>
</section>

<section>
  <h2 class="abs cat-title">Our Categories</h2>
  <p class="abs cat-intro">I must explain to you how all this mistaken idea of denouncing pleasure and praising pain was born and I will give you a complete account of the system, and expound the actual teachings of the great explorer of the truth, the master-builder of human hap</p>

  <div class="abs cat-name" style="right:344px;top:1732px;color:var(--blue)">BLUE CATEGORY</div>
  <div class="abs badge" style="left:876px;top:1719px;background:#d5e4fd"><i style="background:var(--blue)">03</i></div>
  <p class="abs cat-desc" style="right:263px;top:1787px;width:500px">Who have repaid Poor Man's cost of revenue, but are deceptively unprofitable for the business because of how much servicing them costs</p>

  <div class="abs cat-name" style="right:566px;top:1913px;color:var(--teal)">(CENTER OF SOLVENCY)<br>GREEN CATEGORY</div>
  <div class="abs badge" style="left:655px;top:1900px;background:#cdf3ec"><i style="background:var(--teal)">02</i></div>
  <p class="abs cat-desc" style="right:484px;top:1991px;width:400px">Who have repaid Poor Man's cost of revenue and are therefore profitable</p>

  <div class="abs cat-name" style="right:720px;top:2086px;color:var(--red)">RED CATEGORY</div>
  <div class="abs badge" style="left:500px;top:2073px;background:#f9d2d2"><i style="background:var(--red)">01</i></div>
  <p class="abs cat-desc" style="right:638px;top:2141px;width:400px">Who have not repaid what I call "Poor Man's" cost of revenue and are therefore unprofitable</p>

  <a class="btn btn-blue" style="left:464px;top:2253px">Read More</a>
  <a class="btn btn-teal" style="left:609px;top:2253px">Get Started</a>
</section>

<section>
  <div class="abs contact"></div>
  <div class="abs contact-title">GET IN TOUCH<br>WITH US</div>
  <div class="field" style="left:498px;top:2452px">Full Name</div>
  <div class="field" style="left:803px;top:2452px">Email Address</div>
  <div class="field" style="left:498px;top:2520px">Contact Number</div>
  <div class="submit" style="left:803px;top:2520px">Submit Here</div>
</section>

<footer>
  <div class="abs footer"></div>
  <div class="abs brand" style="left:0;top:2740px;width:1200px;justify-content:center;color:var(--white)"><span class="brand-mark"></span>Lumen Ladder Review</div>
  <div class="foot-nav">
    <span style="left:219px">Home</span>
    <span style="left:322px">About Us</span>
    <span style="left:446px">Our Categories</span>
    <span style="left:609px">Testimonials</span>
    <span style="left:758px">Latest Blogs</span>
    <span style="left:905px">Contact Us</span>
  </div>
  <div class="abs social" style="left:549px;top:2867px"></div>
  <div class="abs social" style="left:585px;top:2867px"></div>
  <div class="abs social" style="left:620px;top:2867px"></div>
  <div class="abs copy">© Copyright 2023 | All Rights Reserved.</div>
  <div class="abs chat">
    <svg width="26" height="24" viewBox="0 0 26 24"><path d="M13 2C6.9 2 2 6 2 11c0 2.6 1.3 4.9 3.4 6.5L4.5 22l4.6-2.6c1.2.4 2.5.6 3.9.6 6.1 0 11-4 11-9S19.1 2 13 2z" fill="#fff"/><circle cx="8.5" cy="11" r="1.5" fill="#e2191c"/><circle cx="13" cy="11" r="1.5" fill="#e2191c"/><circle cx="17.5" cy="11" r="1.5" fill="#e2191c"/></svg>
  </div>
</footer>
</body>
</html>
```